BRPS Postcard Design: Mosquito Control, Lawn Maintenance and Pressure washing

I have a new company based in Atlanta,Georgia named Brookvale Pest Shield Services, LLC. We specializes in Mosquito Control. We also have additional services: Lawn maintenance, Pressure Washing and Gutter Cleaning. I would like to see designs with the colors Black, Red, Gray. We would like the customer to think of us when it comes to Enjoying a mosquito free yard and improving the look and feel of their home and lawn.

Industry/Entity Type

It Company

Requirements
Nice to have
• Treatment plans starting at $69/mt - front of card
• The additional services we offer - back of card.

```html
<!DOCTYPE html>
<html lang="en">
<head>
<meta charset="utf-8">
<title>Brookvale Pest Shield Services, LLC — Postcard</title>
<link rel="stylesheet" href="https://fonts.googleapis.com/css2?family=Pinyon+Script&family=Dosis:wght@500&family=Libre+Baskerville:wght@700&display=swap">
<style>
  :root {
    --black: #000000;
    --red: #e82227;
    --band-edge: #dadada;
    --band-fill: #8e8e8e;
    --type-light: #d6d6d6;
    --type-dark: #0a0a0a;
    --insect-dark: #6c6c6c;
    --insect-wing: #d88a78;
  }
  * { margin: 0; padding: 0; box-sizing: border-box; }
  html, body {
    width: 1200px;
    height: 900px;
    overflow: hidden;
    background: var(--black);
  }
  .postcard {
    position: relative;
    width: 1200px;
    height: 900px;
    overflow: hidden;
  }
  .backdrop {
    position: absolute;
    inset: 0;
    width: 1200px;
    height: 900px;
  }
  .backdrop .field-red { fill: var(--red); }
  .backdrop .field-black { fill: var(--black); }
  .backdrop .wave-edge {
    fill: none;
    stroke: var(--band-edge);
    stroke-width: 104;
  }
  .backdrop .wave-fill {
    fill: none;
    stroke: var(--band-fill);
    stroke-width: 76;
  }
  .brand {
    position: absolute;
    left: 74px;
    top: 48px;
    width: 512px;
    text-align: center;
  }
  .brand-name {
    font-family: "Pinyon Script", cursive;
    font-weight: 400;
    font-size: 128px;
    line-height: 1.08;
    color: var(--type-light);
    letter-spacing: 2px;
    white-space: nowrap;
  }
  .brand-rule {
    height: 3px;
    margin: 0 8px 0;
    background: var(--red);
  }
  .brand-tagline {
    margin-top: 6px;
    font-family: "Dosis", sans-serif;
    font-weight: 500;
    font-size: 34px;
    letter-spacing: 1px;
    color: var(--type-light);
    white-space: nowrap;
  }
  .insect-art {
    position: absolute;
    left: 760px;
    top: 340px;
    width: 400px;
    height: 420px;
    border-radius: 48% 48% 44% 44%;
    background: radial-gradient(ellipse at 50% 40%, var(--insect-dark) 0%, var(--insect-dark) 22%, var(--insect-wing) 48%, var(--red) 72%);
  }
  .phone {
    position: absolute;
    left: 500px;
    top: 782px;
    width: 610px;
    text-align: center;
    font-family: "Libre Baskerville", serif;
    font-weight: 700;
    font-size: 72px;
    line-height: 1;
    letter-spacing: 1px;
    color: var(--type-dark);
    white-space: nowrap;
  }
</style>
</head>
<body>
  <main class="postcard">
    <svg class="backdrop" viewBox="0 0 1200 900" aria-hidden="true">
      <rect class="field-red" x="0" y="0" width="1200" height="900"/>
      <path class="field-black" d="M0,0 L1030,0 C930,230 640,310 450,390 C220,490 110,700 75,900 L0,900 Z"/>
      <path class="wave-edge" d="M1035,-20 C930,230 640,310 450,390 C220,490 110,700 72,920"/>
      <path class="wave-fill" d="M1035,-20 C930,230 640,310 450,390 C220,490 110,700 72,920"/>
    </svg>

    <header class="brand">
      <h1 class="brand-name">Brookvale</h1>
      <div class="brand-rule"></div>
      <p class="brand-tagline">Pest Shield Services, LLC</p>
    </header>

    <div class="insect-art" role="img" aria-label="Illustration of a winged insect seen from above, gray body with translucent pink wings"></div>

    <p class="phone">555-014-2290</p>
  </main>
</body>
</html>
```